Evergold Fernbark Inc

Industry/Entity Type

Forestry

Contact Information for Business Card

Company name: Evergold Fernbark INC, Contact Info: Rovelio Marquin, Phone # 541 555 0187, Addres: 284 Willowbend Creek Rd, Ashdale OR 97310, Email: evergoldfernbark@mailbrook.net

```html
<!DOCTYPE html>
<html lang="en">
<head>
<meta charset="utf-8">
<title>Evergold Fernbark INC — Business Card</title>
<link href="https://fonts.googleapis.com/css2?family=Open+Sans:wght@400;600&display=swap" rel="stylesheet">
<style>
  :root {
    --stage: #d3d4d6;
    --card-top: #474747;
    --card-mid: #2a2a2a;
    --card-bottom: #000000;
    --gold: #bd9a5f;
    --ink: #000000;
    --paper: #ffffff;
  }
  * { margin: 0; padding: 0; box-sizing: border-box; }
  html, body {
    width: 1200px; height: 960px; overflow: hidden;
    background: var(--stage);
    font-family: "Open Sans", Arial, sans-serif;
  }
  .canvas { position: relative; width: 1200px; height: 960px; }
  .card {
    position: absolute; width: 750px; height: 428px; overflow: hidden;
    background: linear-gradient(180deg, var(--card-top) 0%, var(--card-mid) 55%, var(--card-bottom) 100%);
    box-shadow: 2px 3px 6px rgba(0,0,0,0.35);
  }
  .card--front { left: 166px; top: 46px; }
  .card--back { left: 242px; top: 498px; }

  .brand { position: absolute; display: flex; align-items: center; gap: 16px; color: var(--gold); font-weight: 600; }
  .brand__dot { width: 100px; height: 100px; border-radius: 50%; border: 14px solid var(--gold); flex: none; }
  .brand__name { line-height: 1; text-transform: uppercase; }
  .brand__line1 { display: block; font-size: 52px; letter-spacing: 2px; }
  .brand__line2 { display: block; font-size: 37px; letter-spacing: 1px; margin-top: 8px; }
  .card--front .brand { left: 38px; top: 56px; }
  .card--back .brand { left: 160px; top: 158px; }

  .contact__tab {
    position: absolute; left: 0; width: 62px; height: 28px;
    background: var(--gold); display: flex; align-items: center; justify-content: flex-end; padding-right: 10px;
  }
  .contact__tab svg { width: 18px; height: 18px; fill: var(--ink); }
  .contact__text { position: absolute; left: 73px; color: var(--paper); font-size: 19px; line-height: 25px; }

  .name-band {
    position: absolute; left: 396px; top: 354px; width: 354px; height: 40px;
    background: var(--gold); color: var(--paper); font-size: 31px; line-height: 40px; padding-left: 48px;
  }
</style>
</head>
<body>
<div class="canvas">
  <section class="card card--front">
    <div class="brand">
      <span class="brand__dot"></span>
      <span class="brand__name"><span class="brand__line1">Evergold</span><span class="brand__line2">Fernbark INC</span></span>
    </div>

    <div class="contact__tab" style="top:267px">
      <svg viewBox="0 0 24 24" aria-hidden="true"><path d="M12 1a8 8 0 0 0-8 8c0 6 8 14 8 14s8-8 8-14a8 8 0 0 0-8-8zm0 11a3 3 0 1 1 0-6 3 3 0 0 1 0 6z"/></svg>
    </div>
    <p class="contact__text" style="top:267px">284 Willowbend Creek Rd,<br>Ashdale OR 97310</p>

    <div class="contact__tab" style="top:334px">
      <svg viewBox="0 0 24 24" aria-hidden="true"><path d="M6.6 10.8a15 15 0 0 0 6.6 6.6l2.2-2.2a1 1 0 0 1 1-.25 11 11 0 0 0 3.6.6 1 1 0 0 1 1 1V20a1 1 0 0 1-1 1A17 17 0 0 1 3 4a1 1 0 0 1 1-1h3.5a1 1 0 0 1 1 1 11 11 0 0 0 .6 3.6 1 1 0 0 1-.25 1z"/></svg>
    </div>
    <p class="contact__text" style="top:334px">541 555 0187</p>

    <div class="contact__tab" style="top:366px">
      <svg viewBox="0 0 24 24" aria-hidden="true"><path d="M2 9l10-6 10 6v11H2zm2 1.2V18h16v-7.8l-8 5z"/></svg>
    </div>
    <p class="contact__text" style="top:366px">evergoldfernbark@mailbrook.net</p>

    <div class="name-band">Rovelio Marquin</div>
  </section>

  <section class="card card--back">
    <div class="brand">
      <span class="brand__dot"></span>
      <span class="brand__name"><span class="brand__line1">Evergold</span><span class="brand__line2">Fernbark INC</span></span>
    </div>
  </section>
</div>
</body>
</html>
```